Kindle Grove Wording For Logo & Business card

I have the logo, I just need the "kindle Grove" wording to go with it, and a business card design. The only thing on the business card is the website info. We provide nature connection experiences, and bolster these efforts through writing and host a platform for community around it.

I also have an idea of what it could look like (sketch), though I'm really not sure how it would come out. I am open to the best design and happy to consider original artwork. You can see what the site is about at KindleGrove.com.

Contact Information for Business Card

The only thing on the business card is the website info and the design. I will put other messaging on the back.

Website lettering (KindleGrove.com) in Montserrat

Logo Text

Kindle Grove (letters optional)

Font styles to use
Other font styles liked:
• montserrat

```html
<!DOCTYPE html>
<html lang="en">
<head>
<meta charset="utf-8">
<title>Kindle Grove Business Card</title>
<link href="https://fonts.googleapis.com/css2?family=Montserrat:wght@300;400;500&display=swap" rel="stylesheet">
<style>
  :root {
    --backdrop: #2f2f31;
    --card-dark: #120d26;
    --card-light: #ffffff;
    --ink: #1b1b1f;
    --rule: #6a6a6a;
    --accent: #f39a1e;
    --white: #ffffff;
    --mark-dark: #1f1640;
  }
  * { box-sizing: border-box; margin: 0; padding: 0; }
  html, body {
    width: 1200px; height: 583px; overflow: hidden;
    background: var(--backdrop);
    font-family: "Montserrat", sans-serif;
  }
  .card {
    position: absolute; top: 154px;
    width: 481px; height: 275px;
    border-radius: 38px;
    overflow: hidden;
  }
  .card-front { left: 94px; background: var(--card-dark); }
  .card-back { left: 627px; background: var(--card-light); color: var(--ink); }

  /* front */
  .front-band {
    position: absolute; left: 0; right: 0; top: 137px;
    height: 0; display: flex; align-items: center;
  }
  .front-rule { height: 2px; background: var(--white); }
  .front-rule.lead { flex: 0 0 74px; }
  .front-rule.trail { flex: 0 0 64px; }
  .front-brand {
    display: flex; align-items: center; gap: 12px;
    margin: 0 14px 0 11px;
  }
  .brand-dot {
    width: 80px; height: 80px; border-radius: 50%;
    background: var(--mark-dark); flex: none;
  }
  .front-name {
    color: var(--white); font-weight: 300; font-size: 27px;
    letter-spacing: 1.5px; white-space: nowrap;
  }

  /* back */
  .back-dot {
    position: absolute; left: 196px; top: 28px;
    width: 88px; height: 88px; border-radius: 50%;
    background: var(--mark-dark);
  }
  .back-name {
    position: absolute; left: 0; right: 0; top: 122px;
    text-align: center; font-weight: 300; font-size: 29px;
    letter-spacing: 1.5px; line-height: 34px;
  }
  .back-rule {
    position: absolute; left: 93px; width: 294px; height: 1px;
    background: var(--rule);
  }
  .website {
    position: absolute; left: 0; right: 0; top: 170px;
    display: flex; justify-content: center; align-items: center; gap: 4px;
    font-size: 16px; line-height: 20px; color: var(--ink);
  }
  .website svg { width: 14px; height: 14px; }
</style>
</head>
<body>
  <section class="card card-front">
    <div class="front-band">
      <span class="front-rule lead"></span>
      <div class="front-brand">
        <span class="brand-dot"></span>
        <span class="front-name">KINDLE GROVE</span>
      </div>
      <span class="front-rule trail"></span>
    </div>
  </section>

  <section class="card card-back">
    <span class="back-dot"></span>
    <h1 class="back-name">KINDLE GROVE</h1>
    <span class="back-rule" style="top:158px"></span>
    <p class="website">
      <svg viewBox="0 0 14 14" aria-hidden="true"><circle cx="7" cy="7" r="7" fill="#f39a1e"/><g fill="none" stroke="#fff" stroke-width=".8"><circle cx="7" cy="7" r="4.5"/><ellipse cx="7" cy="7" rx="2" ry="4.5"/><path d="M2.5 7h9M3.2 4.8h7.6M3.2 9.2h7.6"/></g></svg>
      KindleGrove.com
    </p>
    <span class="back-rule" style="top:202px"></span>
  </section>
</body>
</html>
```